Bright Arch Group business card

Bright Arch Group is the parent company of Bright Arch Building, Bright Arch Plumbing and Bright Arch Renovating. We require a sophisticated business card that covers all aspects of the building and plumbing space without using told or construction items.

Industry/Entity Type

Construction Company

Contact Information for Business Card

Gareth Pimley
Director
0472915083
gareth@brightarch.com.au
Www.brightarch.com.au

Font styles to use
Serif
Sans Serif

Colors
3176b5
ffce3e
0692cd
34a7d8
fbee3e
faa54b

Requirements
Must have
• Logo on front
• Logo and details on rear.
Nice to have
• Maybe water mark or shadow effect with logo
Should not have
• Tools or any construction associated items

```html
<!DOCTYPE html>
<html lang="en">
<head>
<meta charset="utf-8">
<title>Bright Arch Group business card</title>
<link rel="stylesheet" href="https://fonts.googleapis.com/css2?family=Jost:wght@400;500&display=swap">
<style>
  :root {
    --backdrop: #d4d4d4;
    --card: #ffffff;
    --ink: #1d1d1d;
    --accent: #ec7d23;
    --accent-light: #f19228;
    --on-accent: #ffffff;
  }
  html, body {
    margin: 0;
    padding: 0;
    width: 1200px;
    height: 800px;
    overflow: hidden;
    background: var(--backdrop);
    font-family: "Jost", "Helvetica Neue", Arial, sans-serif;
  }
  .stage {
    position: relative;
    width: 1200px;
    height: 800px;
  }
  .card {
    position: absolute;
    top: 283px;
    width: 430px;
    height: 239px;
    background: var(--card);
    overflow: hidden;
  }
  .card--front { left: 110px; }
  .card--back { left: 638px; }

  .brand {
    position: absolute;
    display: flex;
    align-items: center;
    gap: 8px;
    transform: translate(-50%, -50%);
  }
  .card--front .brand { left: 215px; top: 122px; }
  .card--back .brand { left: 115px; top: 122px; }
  .brand__dot {
    width: 14px;
    height: 14px;
    border-radius: 50%;
    background: var(--accent);
    flex: none;
  }
  .brand__name {
    color: var(--ink);
    font-weight: 400;
    font-size: 14px;
    letter-spacing: 0.22em;
    text-transform: uppercase;
    white-space: nowrap;
    line-height: 1;
  }
  .card--back .brand__name { font-size: 12.5px; }

  .details {
    position: absolute;
    left: 213px;
    top: 0;
    width: 217px;
    height: 239px;
    background: linear-gradient(135deg, var(--accent-light) 0%, var(--accent) 35%, var(--accent) 100%);
    color: var(--on-accent);
  }
  .details__name {
    position: absolute;
    left: 52px;
    top: 83px;
    margin: 0;
    font-size: 14px;
    font-weight: 400;
    line-height: 1;
    white-space: nowrap;
  }
  .details__name strong { font-weight: 500; }
  .details__role {
    position: absolute;
    left: 52px;
    top: 99px;
    margin: 0;
    font-size: 4.5px;
    letter-spacing: 0.6em;
    text-transform: uppercase;
  }
  .contact {
    position: absolute;
    left: 52px;
    top: 121px;
    margin: 0;
    padding: 0;
    list-style: none;
    font-size: 7px;
    line-height: 11px;
  }
  .contact__item {
    display: flex;
    align-items: center;
    gap: 4px;
  }
  .contact__icon {
    width: 6px;
    height: 6px;
    flex: none;
  }
</style>
</head>
<body>
<main class="stage">
  <section class="card card--front" aria-label="Card front">
    <div class="brand">
      <span class="brand__dot"></span>
      <span class="brand__name">Bright Arch Group</span>
    </div>
  </section>

  <section class="card card--back" aria-label="Card back">
    <div class="brand">
      <span class="brand__dot"></span>
      <span class="brand__name">Bright Arch Group</span>
    </div>
    <div class="details">
      <h1 class="details__name"><strong>Gareth</strong> Pimley</h1>
      <p class="details__role">Director</p>
      <ul class="contact">
        <li class="contact__item">
          <svg class="contact__icon" viewBox="0 0 10 10" aria-hidden="true"><path d="M2 1 L4 1 L4.6 3 L3.4 4 Q4.5 6 6 6.6 L7 5.4 L9 6 L9 8 Q8 9 7 9 Q1 8 1 2 Q1 1 2 1 Z" fill="none" stroke="currentColor" stroke-width="1"/></svg>
          <span>0472915083</span>
        </li>
        <li class="contact__item">
          <svg class="contact__icon" viewBox="0 0 10 10" aria-hidden="true"><rect x="1" y="2" width="8" height="6" fill="none" stroke="currentColor" stroke-width="1"/><path d="M1 2 L5 5.5 L9 2" fill="none" stroke="currentColor" stroke-width="1"/></svg>
          <span>gareth@brightarch.com.au</span>
        </li>
        <li class="contact__item">
          <svg class="contact__icon" viewBox="0 0 10 10" aria-hidden="true"><circle cx="5" cy="5" r="4" fill="none" stroke="currentColor" stroke-width="1"/><ellipse cx="5" cy="5" rx="1.8" ry="4" fill="none" stroke="currentColor" stroke-width="0.8"/><path d="M1 5 H9" stroke="currentColor" stroke-width="0.8"/></svg>
          <span>www.brightarch.com.au</span>
        </li>
      </ul>
    </div>
  </section>
</main>
</body>
</html>
```